Pinecrest Meadow Collective Memory Wellness Support Office Seeks E-Newsletter Design

We need an electronic newsletter design for regular communication from our organization. We require an editable Mailchimp template that must be optimized for use on mobile phones. For more information about creating a usable and editable HTML Mailchimp template, please read this guide: https://snipvane.com/kWrbTo

The primary audiences for the electronic newsletter are professionals in healthy aging, public health, and brain health. Many of the recipients will be Pinecrest Meadow or Alaska Natives or professionals who provide public health services to Pinecrest Meadow or Alaska Native people.

The e-newsletter design should complement the colors of the Clear Horizon Program project logo. The project logo and color scheme are attached to this design brief. The logo should be at the top of the page.

Attributes that we’d like to come to mind when people our electronic newsletter and think about our organization: professional, informed, trustworthy, respected, innovative, hopeful, positive, welcoming.

We intend to have a combination of written content, videos, and photos. We also will link to outside content.

The e-newsletter will have the following editable sections:
1. Pinecrest Meadow Collective Memory Wellness Support Office Updates: The purpose of the program updates section is for the organization to feature all of the good work accomplished over the month and to highlight why the organization is a leader in aging and brain health.
2. Community Updates: The purpose of the blog section is to promote approaches, programs, policies, funding, relationships, etc. that advance the Clear Horizon Program’s mission and align with the values of organization. This section should make people feel informed, hopeful, and positive. This section will feature photos and should have the ability to feature a video.
3. Advisory Group Feature: The purpose of the Advisory Group Feature section is to highlight the contributions and wealth of experience of our Advisory Group members. This section will feature a photo.
4. Promising Practices: The purpose of the Promising Practices section is to share examples of programs/initiatives/policies that align with the values and mission of the Clear Horizon Program. This section should make people feel informed, hopeful, and positive. This section will also feature
5. Featured Resources: The purpose of the featured resources section is to share resources, upcoming events and opportunities for readers to engage in content that further advances the Clear Horizon Program’s mission. This section will include several links to outside content.
6. Where You Can Find Us: The purpose of the “Where You Can Find Us” section is to share the organization’s contact information and additional ways to engage with the organization and related content. This needs to include links to social media platforms and our website.

Target Market(s)

Font styles to use
Sans Serif

Requirements
Must have
• We require an editable Mailchimp template that is optimized for use on mobile phones. For more information about creating a usable and editable HTML Mailchimp template, please read this guide: https://snipvane.com/kWrbTo
Should not have
• feathers

```html
<!DOCTYPE html>
<html lang="en">
<head>
<meta charset="utf-8">
<title>Pinecrest Meadow Collective Memory Wellness Support Office Newsletter</title>
<link href="https://fonts.googleapis.com/css2?family=Arimo:wght@400;700&family=Lato:wght@400;700&display=swap" rel="stylesheet">
<style>
:root{
  --ink:#111111;
  --body:#333333;
  --muted:#555555;
  --soft-bg:#f4f4f4;
  --teal:#40979f;
  --teal-dark:#2f7780;
  --footer:#0b0b0b;
  --white:#ffffff;
  --icon:#8a8a8a;
  --hero-a:#0a1a5c;
  --hero-b:#1d4fb8;
}
*{margin:0;padding:0;box-sizing:border-box}
html,body{width:1200px;height:4743px;overflow:hidden}
body{position:relative;background:var(--white);font-family:'Lato',sans-serif;color:var(--body)}
.abs{position:absolute}
.section-title{position:absolute;left:0;width:1200px;text-align:center;font-family:'Arimo',sans-serif;font-weight:700;font-size:44px;color:var(--ink);letter-spacing:.5px}

/* hero */
.hero{left:0;top:0;width:1200px;height:644px;background:radial-gradient(circle at 28% 50%,#3b8ce8 0%,var(--hero-b) 28%,var(--hero-a) 75%)}
.hero-art{left:120px;top:110px;width:430px;height:430px;border-radius:50%;background:radial-gradient(circle,#e8577a 0%,#6a3fb0 45%,rgba(40,90,200,0) 72%)}
.brand-mark{display:flex;align-items:center;gap:14px;font-family:'Arimo',sans-serif;font-weight:700;color:var(--white)}
.brand-mark .dot{width:96px;height:96px;border-radius:50%;border:4px solid var(--white);flex:none}
.brand-mark .name{font-size:20px;line-height:1.15;width:300px}
.hero .brand-mark{left:412px;top:16px}
.hero-title{left:565px;top:262px;width:560px;font-family:'Arimo',sans-serif;font-weight:700;color:var(--white);font-size:48px;line-height:1.12;text-transform:uppercase}

/* intro */
.intro-title{top:720px;font-size:37px;line-height:54px;text-transform:uppercase;padding:0 150px}
.intro-text{left:135px;top:845px;width:930px;text-align:center;font-size:27px;line-height:43px;color:var(--body)}

/* community */
.community{left:0;top:1052px;width:1200px;height:1029px;background:var(--soft-bg)}
.card{position:absolute;overflow:hidden;color:var(--white)}
.card .photo{position:absolute;inset:0}
.card .shade{position:absolute;inset:0;background:linear-gradient(to bottom,rgba(0,0,0,0) 45%,rgba(0,0,0,.7) 100%)}
.card h3{position:absolute;left:20px;font-family:'Lato',sans-serif;font-weight:700;font-size:26px}
.card p{position:absolute;left:20px;right:18px;font-size:20px;line-height:30px}
.card.small h3{top:250px}.card.small p{top:292px}
.card.wide h3{top:265px;left:24px}.card.wide p{top:308px;left:24px}
.play{position:absolute;left:50%;top:137px;width:72px;height:72px;margin-left:-36px;border-radius:50%;background:var(--white);box-shadow:0 0 0 6px rgba(255,255,255,.35)}
.play svg{position:absolute;left:26px;top:22px}

/* advisory */
.advisor{position:absolute;top:2258px;width:340px;text-align:center}
.advisor .portrait{width:283px;height:283px;border-radius:50%;margin:0 auto;background:linear-gradient(#d9d9d9,#a6a6a6)}
.advisor h3{margin-top:35px;font-family:'Arimo',sans-serif;font-weight:700;font-size:29px;color:var(--ink)}
.advisor .role{margin-top:8px;font-size:20px;color:var(--muted)}
.advisor .bio{margin-top:18px;font-size:23px;line-height:40px;color:var(--body)}
.advisor .links{margin-top:18px;display:flex;justify-content:center;gap:22px}
.advisor .links span{width:20px;height:20px;border:2px solid var(--icon);border-radius:3px}

/* practices */
.practices{left:0;top:2874px;width:1200px;height:686px;background:var(--teal)}
.practices .section-title{color:var(--white)}
.practice-art{left:75px;top:3019px;width:508px;height:471px;background:radial-gradient(circle at 55% 50%,#5fb0e8 0%,#1f5f9a 40%,#0d2340 100%)}
.practice-list{left:633px;width:520px;color:var(--white)}
.practice-list h3{font-family:'Arimo',sans-serif;font-weight:700;font-size:33px;margin-bottom:12px}
.practice-list li{list-style:none;font-size:24px;line-height:39px;padding-left:33px;position:relative}
.practice-list li::before{content:"";position:absolute;left:8px;top:11px;width:18px;height:18px;border-radius:50%;border:2px solid var(--white);background:radial-gradient(circle,var(--white) 0 4px,transparent 5px)}

/* resources */
.resource{position:absolute;top:3724px;width:500px}
.resource .photo{width:500px;height:355px}
.resource h3{margin-top:28px;font-family:'Arimo',sans-serif;font-weight:700;font-size:29px;color:var(--ink)}
.resource p{margin-top:10px;font-size:20px;line-height:40px;color:var(--muted)}

/* footer */
.footer{left:0;top:4337px;width:1200px;height:406px;background:var(--footer);color:var(--white)}
.footer .brand-mark{position:absolute;left:425px;top:62px}
.footer .brand-mark .dot{width:90px;height:90px}
.contact{position:absolute;left:0;top:192px;width:1200px;text-align:center;font-size:26px}
.social{position:absolute;left:0;top:263px;width:1200px;display:flex;justify-content:center;gap:12px}
.social span{width:56px;height:56px;border:3px solid var(--white);border-radius:50%}
.copyright{position:absolute;left:0;top:350px;width:1200px;text-align:center;font-size:20px}
</style>
</head>
<body>

<header class="abs hero">
  <div class="abs hero-art" role="img" aria-label="Glowing illustration of a human brain on a digital blue background"></div>
  <div class="abs brand-mark"><span class="dot"></span><span class="name">Pinecrest Meadow Collective Memory Wellness Support Office</span></div>
  <h1 class="abs hero-title">Pinecrest Meadow Collective Memory Wellness</h1>
</header>

<h2 class="section-title intro-title">Pinecrest Meadow Collective Memory Wellness Support Office</h2>
<p class="abs intro-text">The purpose of the program updates section is for the organization to feature all of the good work accomplished over the month and to highlight why the organization is a leader in aging and brain health.</p>

<section class="abs community"></section>
<h2 class="section-title" style="top:1125px">COMMUNITY UPDATES</h2>

<article class="card small" style="left:75px;top:1218px;width:335px;height:372px">
  <div class="photo" role="img" aria-label="Smiling couple embracing outdoors in autumn" style="background:linear-gradient(135deg,#c9773a,#7a2a26 60%,#3a1a14)"></div>
  <div class="shade"></div><h3>Heading Here</h3><p>Lorem ipsum met, consectetur adipiscing elit, sed do</p>
</article>
<article class="card small" style="left:432px;top:1218px;width:335px;height:372px">
  <div class="photo" role="img" aria-label="Hand writing with a pen on paper" style="background:linear-gradient(135deg,#e6e6e6,#8c8c8c 55%,#2a2a2a)"></div>
  <div class="shade"></div><h3>Heading Here</h3><p>Lorem ipsum met, consectetur adipiscing elit, sed do</p>
</article>
<article class="card small" style="left:789px;top:1218px;width:335px;height:372px">
  <div class="photo" role="img" aria-label="Seedlings growing on stacks of coins" style="background:linear-gradient(160deg,#d2d5d8,#7c8286 55%,#3a3d40)"></div>
  <div class="shade"></div><h3>Heading Here</h3><p>Lorem ipsum met, consectetur adipiscing elit, sed do</p>
</article>
<article class="card wide" style="left:75px;top:1614px;width:514px;height:388px">
  <div class="photo" role="img" aria-label="Video still of hands at a laptop with data charts" style="background:linear-gradient(135deg,#4a6670,#1f3339 60%,#0e1a1e)"></div>
  <div class="shade"></div>
  <div class="play"><svg width="24" height="28" viewBox="0 0 24 28"><path d="M0 0 L24 14 L0 28Z" fill="#c8202e"/></svg></div>
  <h3>Heading Here</h3><p>Lorem ipsum met, consectetur adipiscing elit, sed do</p>
</article>
<article class="card wide" style="left:611px;top:1614px;width:513px;height:388px">
  <div class="photo" role="img" aria-label="Video still of a group meeting in an office" style="background:linear-gradient(135deg,#b9b5ae,#5c564e 55%,#221f1c)"></div>
  <div class="shade"></div>
  <div class="play"><svg width="24" height="28" viewBox="0 0 24 28"><path d="M0 0 L24 14 L0 28Z" fill="#c8202e"/></svg></div>
  <h3>Heading Here</h3><p>Lorem ipsum met, consectetur adipiscing elit, sed do</p>
</article>

<h2 class="section-title" style="top:2170px">ADVISORY GROUP FEATURE</h2>
<div class="advisor" style="left:73px">
  <div class="portrait" role="img" aria-label="Portrait photo of an advisory group member"></div>
  <h3>JOHN SMITH</h3><p class="role">Quis ipsum suspend</p>
  <p class="bio">Lorem ipsum dolor ser adipiscing elit, sed eiusmor incididunt</p>
  <div class="links"><span></span><span></span><span></span><span></span></div>
</div>
<div class="advisor" style="left:432px">
  <div class="portrait" role="img" aria-label="Portrait photo of an advisory group member"></div>
  <h3>JOHN SMITH</h3><p class="role">Quis ipsum suspend</p>
  <p class="bio">Lorem ipsum dolor ser adipiscing elit, sed eiusmor incididunt</p>
  <div class="links"><span></span><span></span><span></span><span></span></div>
</div>
<div class="advisor" style="left:790px">
  <div class="portrait" role="img" aria-label="Portrait photo of an advisory group member"></div>
  <h3>JOHN SMITH</h3><p class="role">Quis ipsum suspend</p>
  <p class="bio">Lorem ipsum dolor ser adipiscing elit, sed eiusmor incididunt</p>
  <div class="links"><span></span><span></span><span></span><span></span></div>
</div>

<section class="abs practices"></section>
<h2 class="section-title" style="top:2936px;color:var(--white)">PROMISING PRACTICES</h2>
<div class="abs practice-art" role="img" aria-label="Illustration of neurons connecting with electric sparks"></div>
<div class="abs practice-list" style="top:3030px">
  <h3>Our Mission</h3>
  <ul><li>Lorem ipsum dolor sit amet, consectetur</li><li>Adipiscing elit, sed do eempor incididun</li><li>Ut labore et dolore accumsan lacus vel</li><li>Facilisis Lorem ipsum dolor</li></ul>
</div>
<div class="abs practice-list" style="top:3260px">
  <h3>Our Vision</h3>
  <ul><li>Lorem ipsum dolor sit amet, consectetur</li><li>Adipiscing elit, sed do eempor incididun</li><li>Ut labore et dolore accumsan lacus vel</li><li>Facilisis Lorem ipsum dolor</li></ul>
</div>

<h2 class="section-title" style="top:3642px">FEATURED RESOURCES</h2>
<div class="resource" style="left:88px">
  <div class="photo" role="img" aria-label="Woman holding a brain model beside healthy food" style="background:linear-gradient(135deg,#d8a25a,#c98a2a 50%,#8a5a2a)"></div>
  <h3>The standard Lorem Ipsum passage</h3>
  <p>Lorem ipsum dolor sit amet, consectetur adipiscing elit, sed do eiusmod tempor incididunt ut labore et dolore magna aliqua.</p>
</div>
<div class="resource" style="left:611px">
  <div class="photo" role="img" aria-label="Fruits, vegetables and fish arranged in a brain shape" style="background:radial-gradient(circle at 50% 45%,#9ab84a,#c0402a 40%,#2e2e2e 75%)"></div>
  <h3>The standard Lorem Ipsum passage</h3>
  <p>Lorem ipsum dolor sit amet, consectetur adipiscing elit, sed do eiusmod tempor incididunt ut labore et dolore magna aliqua.</p>
</div>

<footer class="abs footer">
  <div class="brand-mark"><span class="dot"></span><span class="name">Pinecrest Meadow Collective Memory Wellness Support Office</span></div>
  <p class="contact">1234 Somestreet Anywhere USA 21212 &nbsp;|&nbsp; 888 888 8888 &nbsp;|&nbsp; info@pinecrestmeadow.org</p>
  <div class="social"><span></span><span></span><span></span><span></span></div>
  <p class="copyright">Copyright 2021 Pinecrest Meadow. All Rights Reserved</p>
</footer>

</body>
</html>
```